Email signature banner for companys 60th anniversary

We are a transportation company. This is what our website people came up with so far:

https://www.plandeckly.com/design/7xQwPz2LmN4rTbVc8HyUoK/Movren?node-id=1830-12

I want a picture of our transport truck with the decal on the back that we are putting on it.

Our website is www.movren.com

Target Market(s)

Customer recognition

Industry/Entity Type

fuel and oil distribution company

Requirements
Must have
• our 60th anniversary logo
Nice to have
• Delivering Energy to Build Communites.
Should not have
• picture of the guy from the current banner provided

```html
<!DOCTYPE html>
<html lang="en">
<head>
<meta charset="utf-8">
<title>60th Anniversary Email Banners</title>
<link href="https://fonts.googleapis.com/css2?family=Bebas+Neue&display=swap" rel="stylesheet">
<style>
  :root {
    --navy: #20386f;
    --sky: #4f8bca;
    --sky-line: #4a8ad0;
    --red: #d2232a;
    --white: #ffffff;
    --page: #ffffff;
  }
  html, body {
    margin: 0;
    padding: 0;
    width: 1200px;
    height: 1200px;
    overflow: hidden;
    background: var(--page);
  }
  .canvas {
    position: relative;
    width: 1200px;
    height: 1200px;
  }
  .banner {
    position: absolute;
    left: 68px;
    width: 1063px;
    height: 267px;
    overflow: hidden;
  }
  .banner--navy { top: 298px; }
  .banner--red { top: 635px; }
  .banner__bg {
    position: absolute;
    inset: 0;
    width: 100%;
    height: 100%;
    display: block;
  }
  .banner__truck {
    position: absolute;
    left: 12px;
    top: 10px;
    width: 355px;
    height: 247px;
    border-radius: 6px;
    background: linear-gradient(135deg, #e9ebee 0%, #b9bec6 45%, #3c4148 80%, #1d2024 100%);
  }
  .banner__headline {
    position: absolute;
    margin: 0;
    font-family: "Bebas Neue", "Oswald", sans-serif;
    font-weight: 400;
    color: var(--white);
    line-height: 1;
    white-space: nowrap;
  }
  .banner__headline .line { position: absolute; left: 0; display: block; }
  .line--small { font-size: 120px; letter-spacing: 1px; }
  .line--large { font-size: 164px; letter-spacing: 2px; }

  .banner--navy .banner__headline { left: 390px; top: 0; }
  .banner--navy .line--small { top: 13px; }
  .banner--navy .line--large { top: 111px; }

  .banner--red .banner__headline { left: 520px; top: 0; }
  .banner--red .line--small { top: 18px; }
  .banner--red .line--large { top: 116px; }
</style>
</head>
<body>
<main class="canvas">

  <section class="banner banner--navy">
    <svg class="banner__bg" viewBox="0 0 1063 267" preserveAspectRatio="none" aria-hidden="true">
      <rect width="1063" height="267" fill="var(--red)"/>
      <path d="M0 0 H879 C960 75 1007 120 1007 180 C1007 215 990 240 962 267 H0 Z" fill="var(--navy)"/>
      <path d="M879 0 C960 75 1007 120 1007 180 C1007 215 990 240 962 267" fill="none" stroke="var(--sky-line)" stroke-width="4"/>
    </svg>
    <div class="banner__truck" role="img" aria-label="Illustration of a fuel tanker truck seen from the rear, with the 60th anniversary decal on the tank"></div>
    <h1 class="banner__headline">
      <span class="line line--small">Celebrating</span>
      <span class="line line--large">60 Years</span>
    </h1>
  </section>

  <section class="banner banner--red">
    <svg class="banner__bg" viewBox="0 0 1063 267" preserveAspectRatio="none" aria-hidden="true">
      <rect width="1063" height="267" fill="var(--red)"/>
      <path d="M0 0 H441 C475 30 486 55 486 86 C486 150 420 205 360 267 H0 Z" fill="var(--sky)"/>
      <path d="M441 0 C475 30 486 55 486 86 C486 150 420 205 360 267" fill="none" stroke="var(--navy)" stroke-width="4"/>
    </svg>
    <div class="banner__truck" role="img" aria-label="Illustration of a fuel tanker truck seen from the rear, with the 60th anniversary decal on the tank"></div>
    <h2 class="banner__headline">
      <span class="line line--small">Celebrating</span>
      <span class="line line--large">60 Years</span>
    </h2>
  </section>

</main>
</body>
</html>
```